Signage for a store*

logo on the two sides of the sign
in the middle is the name of the store witch is VORELT
at the bottom of the two logos, one side for location/address and the other side is contact details phone number is 718-392-6107 address is 2974 THE SIGN WILL BEE 15 FEET BY 4 FEET I WOULD LIKE THAT THE
BACKGROUND OF THE SIGN SHOULD HAVE A NICE COLOR BASE
THAT GOES FOR A WINE STORE

```html
<!DOCTYPE html>
<html lang="en">
<head>
<meta charset="utf-8">
<title>VORELT Store Sign</title>
<link href="https://fonts.googleapis.com/css2?family=Playfair+Display:wght@700&family=Roboto+Slab:wght@400;700&display=swap" rel="stylesheet">
<style>
  :root {
    --stripe-light: #fffad6;
    --stripe-green: #e7eeb0;
    --wine: #a53a55;
    --rose: #e85d7c;
    --gold: #c2a24c;
    --white: #ffffff;
  }
  html, body {
    margin: 0;
    padding: 0;
    width: 1200px;
    height: 320px;
    overflow: hidden;
    background: var(--white);
  }
  .sign {
    position: relative;
    width: 1200px;
    height: 320px;
    overflow: hidden;
    background: var(--white);
  }
  .sign-field {
    position: absolute;
    left: 10px;
    top: 10px;
    width: 1179px;
    height: 299px;
    background: repeating-linear-gradient(
      90deg,
      var(--stripe-light) 0 10px,
      var(--stripe-green) 10px 20px
    );
  }
  .sign-frame {
    position: absolute;
    inset: 0;
  }
  .brand-mark {
    position: absolute;
    top: 50px;
    width: 180px;
    transform: translateX(-50%);
    text-align: center;
  }
  .brand-mark--left { left: 204px; }
  .brand-mark--right { left: 990px; }
  .brand-mark-dot {
    display: block;
    margin: 0 auto 8px;
  }
  .brand-mark-name {
    display: block;
    font-family: "Roboto Slab", serif;
    font-weight: 400;
    font-size: 30px;
    line-height: 1;
    letter-spacing: 1px;
    color: var(--wine);
  }
  .store-name {
    position: absolute;
    left: 0;
    top: 95px;
    width: 1200px;
    margin: 0;
    text-align: center;
    font-family: "Roboto Slab", serif;
    font-weight: 700;
    font-size: 122px;
    line-height: 1;
    color: var(--wine);
    -webkit-text-stroke: 4px var(--rose);
    paint-order: stroke fill;
    text-shadow:
      2px 0 0 var(--white), -2px 0 0 var(--white),
      0 2px 0 var(--white), 0 -2px 0 var(--white),
      2px 2px 0 var(--white), -2px -2px 0 var(--white),
      2px -2px 0 var(--white), -2px 2px 0 var(--white);
  }
  .sign-detail {
    position: absolute;
    top: 216px;
    margin: 0;
    transform: translateX(-50%);
    white-space: nowrap;
    text-align: center;
    font-family: "Playfair Display", serif;
    font-weight: 700;
    font-size: 40px;
    line-height: 1;
    font-variant-numeric: oldstyle-nums;
    color: var(--wine);
  }
  .sign-detail--phone { left: 204px; }
  .sign-detail--address { left: 990px; }
</style>
</head>
<body>
  <main class="sign">
    <div class="sign-field"></div>

    <svg class="sign-frame" width="1200" height="320" viewBox="0 0 1200 320" aria-hidden="true">
      <path d="M61 31 H1140 A30 30 0 0 0 1170 61 V259 A30 30 0 0 0 1140 289 H61 A30 30 0 0 0 30 259 V61 A30 30 0 0 0 61 31 Z"
            fill="none" stroke="var(--wine)" stroke-width="1.2"/>
      <rect x="40.5" y="40.5" width="1119.5" height="239" fill="none" stroke="var(--wine)" stroke-width="1.2"/>
    </svg>

    <div class="brand-mark brand-mark--left">
      <svg class="brand-mark-dot" width="84" height="84" viewBox="0 0 84 84" aria-hidden="true">
        <circle cx="42" cy="42" r="39" fill="none" stroke="var(--gold)" stroke-width="2.5"/>
      </svg>
      <span class="brand-mark-name">VORELT</span>
    </div>

    <h1 class="store-name">VORELT</h1>

    <div class="brand-mark brand-mark--right">
      <svg class="brand-mark-dot" width="84" height="84" viewBox="0 0 84 84" aria-hidden="true">
        <circle cx="42" cy="42" r="39" fill="none" stroke="var(--gold)" stroke-width="2.5"/>
      </svg>
      <span class="brand-mark-name">VORELT</span>
    </div>

    <p class="sign-detail sign-detail--phone">718-392-6107</p>
    <p class="sign-detail sign-detail--address">2974</p>
  </main>
</body>
</html>
```